Construction Finance Company Needs a Magazine Ad

We need a full page magazine ad created for our company, TradeLoftPay. The ad will be featured in RNQB Frame Returns magazine. The audience consists of CFO's, Owners, and Finance Managers for construction companies. We want the ad to be bold, engaging, and eye catching.
Some key points we'd like included (doesn't need to be verbatim ):
Funding the Construction Industry!
-Revolving lines of trade credit (between $15K - $5MM)
-Payment control & tracking platform
-Fast and easy application, no VRSN needed
With TradeLoftPay's unique trade credit system, construction professionals are positioned to manage their cashflow efficiently, grow their businesses, and create new opportunities. Discover our revolutionary system by visiting: www.tradeloftpay-example.com/rnqb
Here are links to our website and the magazine:
Our site: http://tradeloftpay-example.com/
Magazine: http://www.rnqb-example.org/resources/content.cfm?ItemNumber=847&navItemNumber=581
Feel free to checkout our social networks for some additional information/inspiration.
Specs:
Full Page Ad With Bleed
Trim Size: 8.375" x 10.875"
Bleed Size: 8.875" x 11.375"
Live Image Area: 7.625" x 10.125"
All ads containing bleed should have a document size equal to the bleed/trim size. Bleed should be extended 0.25" from the trim on all sides. Crop marks (registration centered) should appear on the ad. Gutter safety: Keep important illustrations or type within a 7.375" x 9.75" live image area. Live copy must not be less than 0.375" from trim size.
Target Market(s)
Owners, CFO's, Credit Managers, CPA's, and Finance Managers of construction companies.
Industry/Entity Type
Construction
Look and feel

```html
<!DOCTYPE html>
<html lang="en">
<head>
<meta charset="utf-8">
<title>TradeLoftPay – Funding the Construction Industry</title>
<link rel="stylesheet" href="https://fonts.googleapis.com/css2?family=Oswald:wght@300;500;700&family=Roboto+Condensed:wght@700&family=Lato:wght@400;700&display=swap">
<style>
  :root {
    --bg: #ece9e4;
    --paper: #ffffff;
    --blue: #1f9ad6;
    --blue-deep: #1579b0;
    --ink: #161616;
    --grey: #5a5a5a;
    --tint: #eef0f2;
    --photo-sky: #3e7fc0;
    --photo-steel: #5d6f80;
    --photo-sunset: #e38a1e;
    --photo-dark: #3a2a12;
  }
  * { margin: 0; padding: 0; box-sizing: border-box; }
  html, body { width: 1200px; height: 1200px; overflow: hidden; background: var(--bg); }
  .ad {
    position: absolute; left: 170px; top: 41px;
    width: 860px; height: 1117px;
    background: var(--paper);
    overflow: hidden;
    box-shadow: 0 4px 20px rgba(0,0,0,.12);
  }
  .ad__art { position: absolute; inset: 0; }
  .headline {
    position: absolute; left: 400px; top: 318px; width: 440px;
    font-family: "Oswald", sans-serif; color: var(--ink); line-height: 1;
  }
  .headline__lead { display: block; font-weight: 700; font-size: 112px; color: #fff; letter-spacing: 1px; }
  .headline__mid { display: block; font-weight: 700; font-size: 40px; margin-top: 6px; letter-spacing: .5px; }
  .headline__end { display: block; font-weight: 300; font-size: 74px; margin-top: 2px; letter-spacing: 1px; }
  .benefits {
    position: absolute; left: 470px; top: 650px; width: 340px; list-style: none;
    font-family: "Roboto Condensed", sans-serif; font-weight: 700; font-size: 17px; color: var(--ink);
    line-height: 1.2;
  }
  .benefits li { position: relative; padding-left: 26px; margin-bottom: 12px; }
  .benefits li::before {
    content: ""; position: absolute; left: 0; top: 5px;
    width: 10px; height: 10px; border-radius: 50%; background: var(--blue);
  }
  .brand { position: absolute; left: 110px; top: 730px; display: flex; align-items: center; gap: 12px; }
  .brand__mark { width: 44px; height: 44px; border-radius: 50%; background: var(--blue); }
  .brand__name { font-family: "Lato", sans-serif; font-weight: 400; font-size: 30px; color: var(--ink); }
  .about {
    position: absolute; left: 90px; top: 800px; width: 360px;
    font-family: "Lato", sans-serif; font-size: 13.5px; line-height: 1.45; color: var(--grey); text-align: justify;
  }
  .site {
    position: absolute; right: 60px; top: 1010px;
    font-family: "Lato", sans-serif; font-size: 15px; letter-spacing: 4px; color: #bdbdbd;
  }
</style>
</head>
<body>
<main class="ad">
  <svg class="ad__art" viewBox="0 0 860 1117" width="860" height="1117">
    <defs>
      <linearGradient id="site-photo" x1="0" y1="0" x2="1" y2="1">
        <stop offset="0" stop-color="var(--photo-sky)"/>
        <stop offset=".55" stop-color="var(--photo-steel)"/>
        <stop offset="1" stop-color="#8a9aa6"/>
      </linearGradient>
      <radialGradient id="sunset-photo" cx=".5" cy=".4" r=".6">
        <stop offset="0" stop-color="#f6b73c"/>
        <stop offset=".7" stop-color="var(--photo-sunset)"/>
        <stop offset="1" stop-color="var(--photo-dark)"/>
      </radialGradient>
    </defs>
    <rect class="blueprint-tint" x="0" y="500" width="860" height="617" fill="var(--tint)" opacity=".55"/>
    <path class="site-photo" role="img" aria-label="Photo: high-rise building under construction with crane and workers in hard hats"
          d="M0,0 H760 C720,190 580,300 390,345 C240,380 100,400 0,470 Z" fill="url(#site-photo)"/>
    <path class="swoosh" d="M0,478 C100,408 240,390 392,356 C592,308 732,196 772,0 H860 V512 C700,560 450,598 0,622 Z"
          fill="var(--blue)" stroke="#fff" stroke-width="10"/>
    <circle cx="205" cy="455" r="112" fill="var(--blue-deep)"/>
    <circle cx="205" cy="455" r="102" fill="#fff"/>
    <circle class="inset-photo" role="img" aria-label="Photo: worker on lifted platform against a sunset sky"
            cx="205" cy="455" r="96" fill="url(#sunset-photo)"/>
    <path class="footer-stripe" d="M860,790 C700,830 520,930 430,1117 H448 C540,945 710,845 860,808 Z" fill="var(--blue)"/>
    <path class="footer" d="M860,820 C710,860 550,960 462,1117 H860 Z" fill="var(--ink)"/>
  </svg>

  <h1 class="headline">
    <span class="headline__lead">FUNDING</span>
    <span class="headline__mid">THE CONSTRUCTION</span>
    <span class="headline__end">INDUSTRY!</span>
  </h1>

  <ul class="benefits">
    <li>Revolving lines of trade credit (between $15K - $5MM)</li>
    <li>Payment control &amp; tracking platform</li>
    <li>Fast and easy application, no VRSN needed</li>
  </ul>

  <div class="brand">
    <span class="brand__mark"></span>
    <span class="brand__name">TradeLoftPay</span>
  </div>

  <p class="about">With TradeLoftPay's unique trade credit system, construction professionals are positioned to manage their cashflow efficiently, grow their businesses, and create new opportunities. Discover our revolutionary system by visiting: www.tradeloftpay-example.com/rnqb</p>

  <p class="site">www.tradeloftpay-example.com</p>
</main>
</body>
</html>
```